Paws and Meadows is a dog walking service that offers home boarding and pet taxi

I am looking for a eye catching A5 leaflet/flyer design for my dog walking business Paws and Meadows.

The flyer must have my company logo on it (jpeg), a picture of my van (jpeg) and a picture of dogs playing (jpegs 1-5).

The fonts must be easy to read. I am not set on any colour scheme but do like the idea of having a natural background. IE. Green grass and blue sky or some forest setting with green trees. If you don't like this idea or its hard to work with don't worry I am open minded so be creative and do what you thinks best.

I'll provide quick feedback to designs that i like and so we can work together.

The flyers must contain the following:

60 minute group and individual walks
GPS Tracked Walks
Home Boarding
Pet Taxi
Puppy/Pet visits

Offer: 50% off first weeks dogs walks with this flyer.

As well as containing my contact info:

07915382046
www.paws-and-meadows.co.uk
paws-and-meadows@mailbrook.co.uk

Chatterbook, Chirpline and Snapgallery logos must be present as well.

Thanks and Good luck!

Target Market(s)

ANYONE WHO NEEDS THEIR DOG WALKED OR LOOKED AFTER WHEN THEY ARE ON HOLIDAY

Industry/Entity Type

Business

Contact Information for Business Card

THE BUSINESS CARD MUST DISPLAY THE LOGO THAT HAS BEEN UPLOADED IN A FILE. IT MUST LOOK SHARP AND PROFESSIONAL. CONTAIN ALL CONTACT INFO AND HAVE SERVICES OFFERED. SEE PROJECT DESCRIPTION FOR FLYER.

Font styles to use
Serif
Sans Serif

Requirements
Must have
• SEE PROJECT DESCRIPTION
Nice to have
• IT WOULD BE NICE TO HAVE PHOTOS OF MY VAN AND DOGS PLAYING. I HAVE UPLOADED SOME PICS OF VAN TO BE USED AND THERE ARE PICS OF DOGS PLAYING THAT COULD BE USED.

```html
<!DOCTYPE html>
<html lang="en">
<head>
<meta charset="utf-8">
<title>Paws and Meadows – Dog Walking Flyer</title>
<link rel="stylesheet" href="https://fonts.googleapis.com/css2?family=Ubuntu:wght@400;500;700&display=swap">
<style>
  :root {
    --purple: #6a2480;
    --yellow: #f4e81f;
    --pink: #e3187c;
    --lime: #9cc41d;
    --paper: #efeded;
    --grass-dark: #3f8a1f;
    --grass: #5fb52e;
    --grass-light: #7fcf3c;
    --white: #ffffff;
  }
  * { box-sizing: border-box; margin: 0; padding: 0; }
  html, body { width: 1200px; height: 927px; overflow: hidden; background: var(--paper); }
  .flyer {
    position: relative; width: 1200px; height: 927px; overflow: hidden;
    font-family: "Ubuntu", sans-serif; background: var(--paper);
  }
  .hero-photo {
    position: absolute; inset: 0 0 180px 0;
    background: linear-gradient(180deg, #2f5d22 0%, #4e8f2a 5%, var(--grass-light) 12%, var(--grass) 45%, var(--grass-dark) 100%);
  }
  .footer-wave { position: absolute; left: 0; top: 630px; width: 1200px; height: 297px; }

  .headline {
    position: absolute; left: 470px; top: -14px;
    transform: rotate(9deg); transform-origin: left top;
    font-weight: 700; text-transform: uppercase; line-height: 1;
  }
  .headline-line {
    display: block; background: var(--purple); color: var(--white);
    font-size: 38px; padding: 16px 40px 6px 34px; width: max-content;
  }
  .headline-line + .headline-line { padding: 6px 34px 18px 34px; }
  .headline .accent { color: var(--yellow); }

  .services-title {
    position: absolute; left: 231px; top: 372px; width: 297px; height: 63px;
    background: var(--purple); color: var(--white);
    font-weight: 500; font-size: 23px; letter-spacing: -0.3px;
    display: flex; align-items: center; justify-content: center;
    clip-path: polygon(0 4%, 100% 0, 100% 88%, 0 100%);
  }
  .services-title .accent { color: var(--yellow); font-weight: 700; }

  .service {
    position: absolute; background: var(--yellow); color: var(--purple);
    font-weight: 700; font-size: 31px; line-height: 1.02; letter-spacing: -0.3px;
    display: flex; align-items: center; padding-left: 22px;
  }
  .service--walks { left: 62px; top: 463px; width: 344px; height: 95px; clip-path: polygon(3% 6%, 100% 0, 98% 92%, 0 100%); }
  .service--gps { left: 62px; top: 561px; width: 318px; height: 64px; clip-path: polygon(0 0, 100% 6%, 99% 100%, 2% 94%); }
  .service--boarding { left: 423px; top: 465px; width: 271px; height: 56px; clip-path: polygon(0 0, 100% 0, 99% 90%, 1% 100%); padding-left: 24px; }
  .service--taxi { left: 423px; top: 524px; width: 168px; height: 49px; clip-path: polygon(0 4%, 100% 0, 97% 100%, 2% 96%); padding-left: 24px; }
  .service--visits { left: 423px; top: 566px; width: 296px; height: 62px; clip-path: polygon(0 8%, 100% 0, 100% 100%, 0 96%); padding-left: 24px; }

  .offer { position: absolute; left: 936px; top: 540px; width: 264px; height: 178px; }
  .offer-shape { position: absolute; inset: 0; }
  .offer-text { position: absolute; left: 14px; top: 8px; color: var(--white); }
  .offer-amount { font-size: 46px; font-weight: 700; letter-spacing: -0.5px; line-height: 1.1; }
  .offer-note { font-size: 17px; font-weight: 400; line-height: 1.15; }

  .van-photo {
    position: absolute; left: 32px; top: 727px; width: 299px; height: 189px;
    border-radius: 14px;
    background: linear-gradient(135deg, #e4e6ea 0%, #ffffff 45%, #3a8fd1 70%, #5aa43a 100%);
  }

  .contact-title {
    position: absolute; left: 444px; top: 739px; width: 154px; height: 47px;
    background: var(--purple); color: var(--yellow);
    font-weight: 700; font-size: 19px;
    display: flex; align-items: center; justify-content: center;
  }
  .contact-list { position: absolute; left: 444px; top: 797px; list-style: none; }
  .contact-item {
    display: flex; align-items: center; height: 32px;
    color: var(--purple); font-size: 18px; font-weight: 500; white-space: nowrap;
  }
  .contact-icon { width: 28px; height: 28px; margin-right: 25px; flex: none; }

  .brand {
    position: absolute; left: 848px; top: 760px; width: 204px;
    display: flex; flex-direction: column; align-items: center;
  }
  .brand-mark { width: 96px; height: 96px; border-radius: 50%; border: 4px solid #f0a81c; }
  .brand-name { margin-top: 12px; font-size: 21px; font-weight: 700; color: #1e1e1e; white-space: nowrap; }

  .social { position: absolute; left: 1062px; top: 764px; list-style: none; }
  .social-item {
    display: flex; align-items: center; height: 34px;
    font-size: 12px; font-weight: 500; color: var(--pink);
  }
  .social-square { width: 24px; height: 24px; background: var(--pink); border-radius: 3px; margin-right: 8px; flex: none; }
</style>
</head>
<body>
<main class="flyer">
  <div class="hero-photo" role="img" aria-label="Photo of a group of dogs playing together on a sunny green park lawn with trees behind"></div>

  <svg class="footer-wave" viewBox="0 0 1200 297" preserveAspectRatio="none" aria-hidden="true">
    <path d="M0 20 C150 10 300 40 430 60 C600 85 700 40 850 45 C1000 50 1100 80 1200 80 L1200 297 L0 297 Z" fill="var(--lime)"/>
    <path d="M0 56 C180 44 320 90 460 98 C620 106 720 72 880 84 C1020 94 1120 110 1200 108 L1200 297 L0 297 Z" fill="var(--paper)"/>
  </svg>

  <h1 class="headline">
    <span class="headline-line"><span class="accent">Take</span> the day <span class="accent">off</span></span>
    <span class="headline-line">We will <span class="accent">take care</span> of your <span class="accent">dog</span></span>
  </h1>

  <h2 class="services-title">THIS ARE OUR&nbsp;<span class="accent">SERVICES:</span></h2>

  <p class="service service--walks">60 minute group<br>and individual walks</p>
  <p class="service service--gps">GPS Tracked Walks</p>
  <p class="service service--boarding">Home Boarding</p>
  <p class="service service--taxi">Pet Taxi</p>
  <p class="service service--visits">Puppy/Pet visits</p>

  <aside class="offer">
    <svg class="offer-shape" viewBox="0 0 264 178" aria-hidden="true">
      <polygon points="0,0 200,0 264,56 264,178 196,127 0,127" fill="var(--pink)"/>
    </svg>
    <div class="offer-text">
      <p class="offer-amount">50 % off</p>
      <p class="offer-note">first weeks dogs walks<br>with this flyer.</p>
    </div>
  </aside>

  <div class="van-photo" role="img" aria-label="Photo of the branded Paws and Meadows van with motion lines around it"></div>

  <h2 class="contact-title">CONTACT US</h2>
  <ul class="contact-list">
    <li class="contact-item">
      <svg class="contact-icon" viewBox="0 0 28 28" aria-hidden="true">
        <rect width="28" height="28" fill="var(--purple)"/>
        <rect x="9" y="5" width="10" height="18" rx="2" fill="none" stroke="var(--yellow)" stroke-width="2"/>
        <circle cx="14" cy="19.5" r="1.2" fill="var(--yellow)"/>
      </svg>07915382046
    </li>
    <li class="contact-item">
      <svg class="contact-icon" viewBox="0 0 28 28" aria-hidden="true">
        <rect width="28" height="28" fill="var(--purple)"/>
        <circle cx="14" cy="14" r="8" fill="none" stroke="var(--yellow)" stroke-width="1.8"/>
        <ellipse cx="14" cy="14" rx="3.5" ry="8" fill="none" stroke="var(--yellow)" stroke-width="1.5"/>
        <line x1="6" y1="14" x2="22" y2="14" stroke="var(--yellow)" stroke-width="1.5"/>
      </svg>www.paws-and-meadows.co.uk
    </li>
    <li class="contact-item">
      <svg class="contact-icon" viewBox="0 0 28 28" aria-hidden="true">
        <rect width="28" height="28" fill="var(--purple)"/>
        <rect x="5" y="8" width="18" height="12" fill="var(--yellow)"/>
        <polyline points="5,8 14,15 23,8" fill="none" stroke="var(--purple)" stroke-width="1.6"/>
      </svg>paws-and-meadows@mailbrook.co.uk
    </li>
  </ul>

  <div class="brand">
    <span class="brand-mark" aria-hidden="true"></span>
    <p class="brand-name">Paws and Meadows</p>
  </div>

  <ul class="social">
    <li class="social-item"><span class="social-square" aria-hidden="true"></span>Chatterbook</li>
    <li class="social-item"><span class="social-square" aria-hidden="true"></span>Chirpline</li>
    <li class="social-item"><span class="social-square" aria-hidden="true"></span>Snapgallery</li>
  </ul>
</main>
</body>
</html>
```